SEAFOOD PACKAGING (Products for consumer)

We are looking to create packaging for various seafood products such as octopus and squid. We plan to sell our products in upscale supermarkets.

We are specializing in cut octopus this time.

Please include our company logo. Also, please leave a transparent area so that customers can see the product inside.
Updates

We want to show what is inside, so a picture of the octopus is not required. We need something simple and sophisticated.

Target Market(s)

upscale store in US and ASIA

Industry/Entity Type

Fisheries dealer

Requirements
Must have
• Please include the attached logo,Blue one is preferred.Please leave a transparent part so that the contents of the product can be seen by the consumer.1. product name on packaging →CUT OCTOPUS,TAKO SASHIMI,Highest quality,Top quality etc... 3. What text information should be on the packaging →(It may be edited, but this is the image) The raw materials are caught in a very clean environment and processed in a modern factory with ZEK certification. We are committed to additive-free products. 4. Packing size(cm/inch)→it will be about 19cm*22cm. 5. what kind of packaging do you use →PP or PA 6. dll →ai,jag
Nice to have
• https://quillmora.example/shots/4829174-Velka-Reef We need something simple and sophisticated like this one.
Should not have
• We want to show what is inside, so a picture of the octopus is not required. We need something simple and sophisticated.

```html
<!DOCTYPE html>
<html lang="en">
<head>
<meta charset="utf-8">
<title>Norva Cut Octopus – Tako Sashimi Pouch</title>
<link href="https://fonts.googleapis.com/css2?family=Oswald:wght@300;400;600&family=Kaushan+Script&family=Montserrat:wght@500&display=swap" rel="stylesheet">
<style>
  :root {
    --stage: #efefef;
    --pouch-edge: #a9d8ec;
    --pouch-mid: #d6eef7;
    --pouch-light: #f7fbfd;
    --brand-blue: #1f56a3;
    --ribbon-blue: #1e63b3;
    --ribbon-dark: #154b8c;
    --accent-red: #dc1a22;
    --body-grey: #6d7780;
    --ink-dark: #4b5560;
    --white: #ffffff;
  }
  * { margin: 0; padding: 0; box-sizing: border-box; }
  html, body { width: 1200px; height: 1200px; overflow: hidden; background: var(--stage); }
  .canvas { position: relative; width: 1200px; height: 1200px; }

  .pouch {
    position: absolute; left: 216px; top: 124px; width: 768px; height: 952px;
    background:
      radial-gradient(ellipse 52% 48% at 40% 50%, var(--pouch-light) 0%, var(--pouch-light) 45%, rgba(247,251,253,0) 100%),
      linear-gradient(180deg, var(--pouch-edge) 0%, var(--pouch-mid) 30%, var(--pouch-mid) 70%, var(--pouch-edge) 100%);
  }

  .brand-name {
    position: absolute; left: 0; width: 470px; top: 211px; text-align: center;
    font-family: 'Oswald', sans-serif; font-weight: 600; font-size: 46px; line-height: 1;
    letter-spacing: 6px; color: var(--brand-blue);
  }

  .product-name {
    position: absolute; left: 0; width: 470px; top: 310px; text-align: center;
    font-family: 'Oswald', sans-serif; font-weight: 600; font-size: 54px;
    line-height: 1; color: var(--brand-blue);
  }

  .product-subtitle {
    position: absolute; left: 0; width: 470px; top: 388px; text-align: center;
    font-family: 'Kaushan Script', cursive; font-size: 50px; line-height: 0.95;
    color: var(--accent-red);
  }
  .subtitle-swash { position: absolute; left: 189px; top: 480px; }

  .product-story {
    position: absolute; left: 95px; width: 284px; top: 546px; text-align: center;
    font-family: 'Oswald', sans-serif; font-weight: 300; font-size: 13px;
    line-height: 17.5px; color: var(--body-grey); text-transform: uppercase;
  }

  .quality-band { position: absolute; left: 57px; top: 652px; }

  .pack-info {
    position: absolute; top: 793px; left: 133px; display: flex; align-items: center; gap: 12px;
    font-family: 'Montserrat', sans-serif; font-weight: 500; font-size: 12px;
    line-height: 15px; color: var(--ink-dark);
  }
  .pack-divider { width: 2px; height: 24px; background: var(--accent-red); }
  .storage { display: flex; align-items: center; gap: 6px; }

  .product-window {
    position: absolute; left: 460px; top: 154px; width: 240px; height: 639px;
    border-radius: 120px;
    background: linear-gradient(170deg, #f4eeee 0%, #efe2e1 25%, #f3e9e8 50%, #eedcda 75%, #f5eeee 100%);
    box-shadow: inset 0 0 0 1px rgba(255,255,255,0.7);
  }
</style>
</head>
<body>
<main class="canvas">
  <section class="pouch">
    <div class="brand-name">NORVA</div>

    <h1 class="product-name">CUT OCTOPUS</h1>
    <p class="product-subtitle">Tako<br>Sashimi</p>
    <svg class="subtitle-swash" width="150" height="44" viewBox="0 0 150 44" aria-hidden="true">
      <path d="M4 40 C10 30, 40 24, 80 22 C110 20, 132 14, 146 2 C136 20, 112 28, 80 30 C45 32, 20 34, 4 40 Z" fill="var(--accent-red)"/>
    </svg>

    <p class="product-story">The raw materials are caught in a very clean environment and processed in a modern factory with ZEK certification. We are committed to additive-free products.</p>

    <svg class="quality-band" width="360" height="112" viewBox="0 0 360 112" aria-label="Premium quality seal: 100% natural, no added preservatives">
      <polygon points="8,31 120,31 120,91 0,91 10,61" fill="var(--ribbon-blue)"/>
      <polygon points="235,31 350,31 340,61 352,91 235,91" fill="var(--ribbon-blue)"/>
      <polygon points="10,86 120,86 120,91 0,91" fill="var(--ribbon-dark)"/>
      <text x="68" y="57" text-anchor="middle" font-family="Oswald, sans-serif" font-weight="300" font-size="14" fill="#fff">100%</text>
      <text x="68" y="74" text-anchor="middle" font-family="Oswald, sans-serif" font-weight="300" font-size="14" fill="#fff">NATURAL</text>
      <text x="290" y="57" text-anchor="middle" font-family="Oswald, sans-serif" font-weight="300" font-size="14" fill="#fff">NO ADDED</text>
      <text x="290" y="74" text-anchor="middle" font-family="Oswald, sans-serif" font-weight="300" font-size="14" fill="#fff">PRESERVATIVES</text>
      <circle cx="177" cy="56" r="54" fill="#fff"/>
      <circle cx="177" cy="56" r="50" fill="var(--accent-red)"/>
      <path id="sealTop" d="M142 56 A35 35 0 0 1 212 56" fill="none"/>
      <path id="sealBottom" d="M139 60 A38 38 0 0 0 215 60" fill="none"/>
      <text font-family="Montserrat, sans-serif" font-weight="500" font-size="11" fill="#fff" letter-spacing="1">
        <textPath href="#sealTop" startOffset="50%" text-anchor="middle">PREMIUM</textPath>
      </text>
      <text font-family="Montserrat, sans-serif" font-weight="500" font-size="11" fill="#fff" letter-spacing="1">
        <textPath href="#sealBottom" startOffset="50%" text-anchor="middle">QUALITY</textPath>
      </text>
      <circle cx="177" cy="53" r="12" fill="none" stroke="#fff" stroke-width="2.5"/>
      <polyline points="171,64 168,76 173,73 177,77" fill="none" stroke="#fff" stroke-width="2"/>
      <polyline points="183,64 186,76 181,73 177,77" fill="none" stroke="#fff" stroke-width="2"/>
    </svg>

    <div class="pack-info">
      <div class="net-weight">NET WT. XX.X LB.<br>(YYY OZ) ZZZ GM.</div>
      <span class="pack-divider"></span>
      <div class="storage">
        <svg width="22" height="22" viewBox="0 0 24 24" aria-hidden="true" stroke="var(--ribbon-blue)" stroke-width="2" stroke-linecap="round">
          <line x1="12" y1="2" x2="12" y2="22"/><line x1="3.3" y1="7" x2="20.7" y2="17"/><line x1="3.3" y1="17" x2="20.7" y2="7"/>
          <polyline points="9,4 12,6.5 15,4" fill="none"/><polyline points="9,20 12,17.5 15,20" fill="none"/>
        </svg>
        <span>KEEP<br>FROZEN</span>
      </div>
    </div>

    <div class="product-window" role="img" aria-label="Clear window showing the frozen cut octopus pieces inside the pouch"></div>
  </section>
</main>
</body>
</html>
```